immediate money for financial solutions

We need a Clean yet, eye catching, Business Card denoting a professional financial/tech firm. The front should have our logo and the notion that we are money lenders that get business loans quickly & easily. Maybe shade the colors of our logo. We are opened, but not committed to an unusual shaped card. The Back Should have our Business Contact Info & logo found on our website's front page: TALVOROINC.COM

Financial

```html
<!DOCTYPE html>
<html lang="en">
<head>
<meta charset="utf-8">
<title>Talvoro Inc — Business Card</title>
<link href="https://fonts.googleapis.com/css2?family=Roboto:wght@300;400;500;700&display=swap" rel="stylesheet">
<style>
  :root {
    --backdrop: #ececec;
    --card: #ffffff;
    --brand-green: #1f9a45;
    --band-teal: #17987a;
    --ink-grey: #8a8a8a;
    --ink-light: #a3a3a3;
    --icon-green: #2fae4f;
    --pattern-top: #58d25f;
    --pattern-mid: #7fdc9a;
    --pattern-low: #2fb8b0;
  }
  * { box-sizing: border-box; margin: 0; padding: 0; }
  html, body { width: 1200px; height: 1000px; overflow: hidden; }
  body {
    background: var(--backdrop);
    font-family: "Roboto", Arial, sans-serif;
    position: relative;
  }
  .card {
    position: absolute;
    top: 350px;
    width: 520px;
    height: 300px;
    box-shadow: 0 6px 18px rgba(0,0,0,0.12);
    overflow: hidden;
  }
  .card--front { left: 60px; background: var(--card); }
  .card--back { left: 620px; }

  .brand {
    position: absolute;
    left: 40px;
    top: 116px;
    color: var(--brand-green);
    font-weight: 500;
    font-size: 34px;
    letter-spacing: 1px;
  }
  .contact {
    position: absolute;
    left: 316px;
    top: 110px;
  }
  .contact__name {
    color: var(--ink-grey);
    font-weight: 300;
    font-size: 22px;
    letter-spacing: 0.5px;
  }
  .contact__title {
    color: var(--brand-green);
    font-weight: 700;
    font-size: 15px;
    margin-bottom: 14px;
  }
  .contact__row {
    display: flex;
    align-items: flex-start;
    gap: 8px;
    color: var(--ink-light);
    font-weight: 300;
    font-size: 14px;
    line-height: 20px;
  }
  .contact__row svg { flex: none; margin-top: 3px; }
  .contact__lines { display: flex; flex-direction: column; }
  .contact__row + .contact__row { margin-top: 4px; }

  .tagline-band {
    position: absolute;
    left: 0; right: 0; bottom: 0;
    height: 36px;
    background: var(--band-teal);
    color: #ffffff;
    font-size: 12.5px;
    font-weight: 300;
    line-height: 36px;
    padding-left: 40px;
  }

  .pattern {
    width: 100%;
    height: 100%;
    background:
      radial-gradient(ellipse at 45% 30%, var(--pattern-top) 0%, rgba(88,210,95,0) 60%),
      linear-gradient(160deg, var(--pattern-mid) 0%, var(--pattern-top) 35%, var(--pattern-mid) 60%, var(--pattern-low) 100%);
  }
</style>
</head>
<body>
  <section class="card card--front" aria-label="Card front">
    <div class="brand">TALVORO INC</div>

    <div class="contact">
      <div class="contact__name">DANIEL MARSH</div>
      <div class="contact__title">President / Lender</div>
      <div class="contact__row">
        <svg width="14" height="14" viewBox="0 0 24 24" aria-hidden="true">
          <path fill="var(--icon-green)" d="M6.6 10.8c1.4 2.8 3.8 5.1 6.6 6.6l2.2-2.2c.3-.3.7-.4 1-.2 1.1.4 2.3.6 3.6.6.6 0 1 .4 1 1V20c0 .6-.4 1-1 1C10.6 21 3 13.4 3 4c0-.6.4-1 1-1h3.5c.6 0 1 .4 1 1 0 1.3.2 2.5.6 3.6.1.3 0 .7-.2 1z"/>
        </svg>
        <span>555.014.2238</span>
      </div>
      <div class="contact__row">
        <svg width="14" height="14" viewBox="0 0 24 24" aria-hidden="true">
          <circle cx="12" cy="12" r="10" fill="none" stroke="var(--icon-green)" stroke-width="2"/>
          <path d="M2 12h20M12 2c3 3 3 17 0 20M12 2c-3 3-3 17 0 20M4 7h16M4 17h16" fill="none" stroke="var(--icon-green)" stroke-width="1.5"/>
        </svg>
        <div class="contact__lines">
          <span>Daniel@talvoroinc.com</span>
          <span>ATMinfo@talvoroinc.com</span>
        </div>
      </div>
    </div>

    <div class="tagline-band">I.O.C.Agent RQN Inc.Backed Financial Provider A.S.A.P Lender</div>
  </section>

  <section class="card card--back" aria-label="Card back">
    <div class="pattern" role="img" aria-label="Repeating green and teal isometric cube pattern"></div>
  </section>
</body>
</html>
```